New Hair Product Line needs Logo and packaging design

We need a logo and package design for our hair system called "Tulip Hair Solutions."
Our 2 part systems includes an 8 oz. "Dawn Dew" Spray and a 4 oz "Moon - Glow Renew" scalp serum. It is a morning/ evening hair growth system for wavy, curly or coiled hair.
Our target market are women ages 18-65 who are very busy and experience the challenges of growing out and controlling their curly hair. But are not willing to sacrifice a good hair day, just because they are busy.
We would like the 2 products to appeal to women, have a unified packaging as well as ,we are looking for an elegant and modern feel.
This packaging will be on retail shelves of Brightmart, Pellford and DkR. as well as LMB..the shopping channel

Brightmart Market(s)

Busy Women ages 18-65 with wavy, curly or coiled hair

Industry/Entity Type

Hair Care Product

Logo Text

Tulip Hair Solutions... Since Curls Count!

Font styles to use
Decorative

Requirements
Must have
• Sulfate Free
• Distributed by Cobalt Lane Beauty LLC
• Nesconset, NY
• Barcode and UPC Number

```html
<!DOCTYPE html>
<html lang="en">
<head>
<meta charset="utf-8">
<title>Tulip Hair Solutions – Dawn Dew &amp; Moon-Glow Renew</title>
<link href="https://fonts.googleapis.com/css2?family=Questrial&family=Josefin+Sans:wght@600&display=swap" rel="stylesheet">
<style>
  :root {
    --backdrop: #e6e6e6;
    --bottle-light: #ffffff;
    --bottle-shade: #dcdcdc;
    --pump: #161616;
    --pump-top: #2a2a2a;
    --ink-dark: #333333;
    --ink-mid: #555555;
    --ink-soft: #8a8a8a;
    --badge: #7d7d7d;
    --badge-text: #ffffff;
  }
  * { margin: 0; padding: 0; box-sizing: border-box; }
  html, body { width: 1200px; height: 1200px; overflow: hidden; }
  body {
    background: var(--backdrop);
    position: relative;
    font-family: "Questrial", sans-serif;
  }
  .bottle { position: absolute; }
  .pump {
    position: absolute;
    left: 50%;
    transform: translateX(-50%);
    background: var(--pump);
    border-radius: 3px 3px 0 0;
  }
  .pump-head {
    position: absolute;
    left: 50%;
    transform: translateX(-50%);
    background: var(--pump-top);
    border-radius: 8px 14px 0 0;
  }
  .bottle-body {
    position: absolute;
    left: 0; right: 0; bottom: 0;
    border-radius: 60px 60px 14px 14px;
    background: linear-gradient(90deg, var(--bottle-shade) 0%, var(--bottle-light) 22%, var(--bottle-light) 70%, var(--bottle-shade) 100%);
    overflow: hidden;
  }
  .label-pattern {
    position: absolute; inset: 0;
    background: radial-gradient(ellipse at 40% 30%, rgba(255,255,255,0.9), rgba(225,225,225,0.6) 70%);
  }
  .label-band {
    position: absolute; left: 0; right: 0;
    background: rgba(255,255,255,0.55);
  }
  .label-text { position: absolute; left: 0; right: 0; text-align: center; }
  .brand-name {
    font-family: "Josefin Sans", sans-serif;
    font-weight: 600;
    color: var(--ink-dark);
    line-height: 1;
    letter-spacing: 0.02em;
  }
  .brand-sub {
    font-family: "Josefin Sans", sans-serif;
    font-weight: 600;
    color: var(--ink-dark);
    letter-spacing: 0.12em;
    line-height: 1;
  }
  .product-name {
    color: var(--ink-mid);
    font-size: 23px;
    letter-spacing: 0.08em;
    line-height: 30px;
    text-transform: uppercase;
  }
  .product-type {
    color: var(--ink-soft);
    font-size: 13px;
    letter-spacing: 0.04em;
    margin-top: 8px;
    text-transform: uppercase;
  }
  .claim {
    color: var(--ink-soft);
    font-size: 13px;
    line-height: 18px;
    letter-spacing: 0.02em;
    text-transform: uppercase;
  }
  .size-badge {
    position: absolute;
    left: 50%;
    width: 50px; height: 50px;
    margin-left: -25px;
    border-radius: 50%;
    background: var(--badge);
    color: var(--badge-text);
    font-size: 15px;
    display: flex; align-items: center; justify-content: center;
  }
</style>
</head>
<body>

  <!-- 8 oz spray -->
  <div class="bottle bottle--spray" style="left:303px; top:105px; width:278px; height:1018px;">
    <div class="pump-head" style="top:0; width:120px; height:40px;"></div>
    <div class="pump" style="top:34px; width:152px; height:250px;"></div>
    <div class="bottle-body" style="height:744px;">
      <div class="label-pattern" role="img" aria-label="Flowing line pattern of curly hair strands"></div>
      <div class="label-band" style="top:373px; height:110px;"></div>
      <div class="label-text" style="top:136px;">
        <div class="brand-name" style="font-size:44px;">TULIP</div>
        <div class="brand-sub" style="font-size:11px; margin-top:4px;">HAIR SOLUTIONS</div>
      </div>
      <div class="label-text" style="top:382px;">
        <div class="product-name">Dawn<br>Dew</div>
        <div class="product-type">Spray</div>
      </div>
      <div class="label-text claim" style="top:570px;">Hair growth system<br>for wavy, curly or<br>coiled hair</div>
      <div class="size-badge" style="top:672px;">8oz</div>
    </div>
  </div>

  <!-- 4 oz scalp serum -->
  <div class="bottle bottle--serum" style="left:696px; top:249px; width:238px; height:874px;">
    <div class="pump-head" style="top:0; width:100px; height:34px;"></div>
    <div class="pump" style="top:28px; width:133px; height:204px;"></div>
    <div class="bottle-body" style="height:642px;">
      <div class="label-pattern" role="img" aria-label="Flowing line pattern of curly hair strands"></div>
      <div class="label-band" style="top:271px; height:110px;"></div>
      <div class="label-text" style="top:117px;">
        <div class="brand-name" style="font-size:37px;">TULIP</div>
        <div class="brand-sub" style="font-size:9.5px; margin-top:4px;">HAIR SOLUTIONS</div>
      </div>
      <div class="label-text" style="top:280px;">
        <div class="product-name">Moon-Glow<br>Renew</div>
        <div class="product-type">Scalp Serum</div>
      </div>
      <div class="label-text claim" style="top:468px;">Hair growth system<br>for wavy, curly or<br>coiled hair</div>
      <div class="size-badge" style="top:570px;">4oz</div>
    </div>
  </div>

</body>
</html>
```